Regenerative Wellness Flyer to recruit Dr offices and clinics

This is a flyer that will be used to recruit new Dr offices and clinics to make them aware of a brand new product that is about to hit the market.

I uploaded an older flyer that I do like. This product is not Stem Cells but fixes a lot of the same things. So the title could be Regenerative Wellness and Cell Factor Therapy.

I also loaded a multiple page info on the product.

I would like to be able to change out logo's & contact information as I have a couple sales people helping push this. I also attached my logo, Velmora. Would like to be able to a QR code...

This is the landing page that the flyer will drive Dr's to:
https://app.pagebrixel.com/v2/preview/K3QwzRtuNaLmBv8Hp2Dx?notrack=true

Target Market(s)

Dr's office, clinics, alternative wellness clinics

Industry/Entity Type

health & wellness

Colors
0054AA
0677BA
7BADD7
CADEEF
E8F1F8
00AB8E
00BBA5
67D7C9
C6EFE9
E9F9F6

Requirements
Nice to have
• The ability to change out the logo/contact info areas

```html
<!DOCTYPE html>
<html lang="en">
<head>
<meta charset="utf-8">
<title>Velmora Wellness – Regenerative Wellness and Cell Factor Therapy</title>
<link href="https://fonts.googleapis.com/css2?family=Poppins:wght@400;500;600;700&display=swap" rel="stylesheet">
<style>
:root{
  --navy:#0054AA;
  --blue:#0677BA;
  --sky:#7BADD7;
  --ice:#CADEEF;
  --frost:#E8F1F8;
  --teal:#00AB8E;
  --aqua:#00BBA5;
  --mint:#67D7C9;
  --foam:#C6EFE9;
  --spray:#E9F9F6;
  --ink:#1f2430;
  --paper:#ffffff;
}
*{box-sizing:border-box;margin:0;padding:0}
html,body{width:940px;height:1200px;overflow:hidden;background:var(--paper)}
body{font-family:'Poppins',sans-serif;color:var(--ink)}
.flyer{position:relative;width:940px;height:1200px;overflow:hidden;
  background:linear-gradient(180deg,var(--paper) 0%,var(--paper) 70%,var(--frost) 100%)}
.abs{position:absolute}

/* brand */
.brand{left:92px;top:84px;width:160px;text-align:center}
.brand-dot{width:120px;height:120px;border-radius:50%;background:var(--foam);margin:0 auto 12px}
.brand-name{font-weight:600;font-size:16px;color:var(--teal)}

/* hero */
.hero-arc{left:528px;top:96px;width:444px;height:444px;border-radius:50%;background:var(--foam)}
.hero-photo{left:515px;top:86px;width:444px;height:444px;border-radius:50%;
  background:linear-gradient(135deg,var(--ice) 0%,var(--frost) 50%,var(--sky) 100%);
  border:4px solid var(--paper)}
.title{left:67px;top:245px;font-size:44px;line-height:50px;letter-spacing:-.3px}
.title .light{font-weight:400;color:var(--teal)}
.title .teal{font-weight:700;color:var(--teal)}
.title .navy{font-weight:700;color:var(--navy)}
.title-rule{left:67px;top:463px;width:34px;height:4px;background:var(--navy)}
.lede{left:67px;font-size:14px;line-height:19px;font-weight:500;width:330px}
.lede-1{top:485px}
.lede-2{top:540px}

/* features */
.features{left:0;top:593px;width:420px;height:284px;background:var(--navy);border-radius:0 24px 24px 0}
.feature{position:absolute;width:170px;text-align:center;color:#fff;font-weight:600;font-size:13.5px;line-height:18px}
.feature .icon{width:64px;height:64px;border-radius:50%;background:var(--foam);border:4px solid var(--mint);
  margin:0 auto 12px;display:flex;align-items:center;justify-content:center}
.f1{left:66px;top:18px}.f2{left:236px;top:18px}
.f3{left:66px;top:150px}.f4{left:236px;top:150px}
.v-rule{position:absolute;left:230px;border-left:1px dashed rgba(255,255,255,.8)}
.h-rule{position:absolute;top:130px;width:148px;border-top:1px dashed rgba(255,255,255,.8)}

/* complete therapy */
.sub-head{left:67px;top:888px;font-size:22px;line-height:28px;font-weight:700;color:var(--teal);width:340px}
.body-copy{left:67px;top:947px;width:345px;font-size:10.3px;line-height:14px}
.tag-bar{left:67px;top:1105px;width:351px;height:20px;background:var(--navy);border-radius:3px;
  color:#fff;font-size:9.5px;display:flex;justify-content:space-around;align-items:center}

/* regulation */
.reg-head{left:471px;top:547px;font-size:25px;line-height:30px;font-weight:700;color:var(--teal);width:420px}
.reg-copy{left:471px;top:612px;width:398px;font-size:13.6px;line-height:17.8px}
.dash{left:471px;width:396px;border-top:1px dashed var(--navy)}
.dash-1{top:736px}.dash-2{top:967px}

.label{width:148px;text-align:center}
.label .top{border:1.5px solid var(--navy);border-radius:4px;font-size:11px;font-weight:600;color:var(--teal);
  padding:1px 0;background:#fff}
.label .bottom{background:var(--navy);color:var(--spray);font-weight:600;font-size:12px;border-radius:3px;padding:2px 0;margin-top:2px}
.label-form{left:471px;top:767px}
.label-apps{left:716px;top:762px}

.vial{left:625px;top:774px}
.checks{list-style:none;font-size:12.5px;line-height:15px;font-weight:600}
.checks li{position:relative;padding-left:16px;margin-bottom:16px}
.checks li::before{content:"";position:absolute;left:0;top:3px;width:9px;height:9px;border-radius:50%;background:var(--teal)}
.checks li::after{content:"";position:absolute;left:2.5px;top:5.5px;width:4px;height:2px;border-left:1.3px solid #fff;border-bottom:1.3px solid #fff;transform:rotate(-45deg)}
.checks-form{left:471px;top:824px;width:145px}
.checks-apps{left:716px;top:824px;width:145px}

/* contact */
.contact-head{left:471px;top:987px;font-size:22px;font-weight:700;color:var(--navy)}
.contact-head span{font-weight:400;color:var(--teal)}
.contact-line{left:471px;display:flex;align-items:center;gap:12px}
.phone{top:1034px;font-size:22px;font-weight:700}
.email{top:1077px;font-size:17px;letter-spacing:.5px}
.web{top:1108px;font-size:18px;letter-spacing:3px}
.web b{color:var(--navy);font-weight:700}
.ico{width:20px;height:20px;border-radius:50%;background:var(--teal);display:flex;align-items:center;justify-content:center;flex:none}
.ico.sm{width:14px;height:14px;margin:0 3px}
.qr{left:800px;top:1036px;width:66px;height:66px;background:#fff;border:2px solid var(--navy);border-radius:4px}
</style>
</head>
<body>
<main class="flyer">

  <div class="abs hero-arc"></div>
  <div class="abs hero-photo" role="img" aria-label="Photo of a clinician in a white coat and gloves performing a facial treatment on a reclining patient"></div>

  <div class="abs brand">
    <div class="brand-dot"></div>
    <div class="brand-name">Velmora Wellness</div>
  </div>

  <h1 class="abs title">
    <span class="light">Regenerative</span><br>
    <span class="teal">Wellness and</span><br>
    <span class="navy">Cell Factor</span><br>
    <span class="navy">Therapy</span>
  </h1>
  <div class="abs title-rule"></div>

  <p class="abs lede lede-1">Concerned about FDA stronghold in regenerative medicine?</p>
  <p class="abs lede lede-2">A powerful &amp; safe new to market approach: FREE from regulatory constraints</p>

  <section class="abs features">
    <div class="feature f1">
      <div class="icon"><svg width="26" height="32" viewBox="0 0 26 32" fill="none" stroke="#0054AA" stroke-width="1.8"><rect x="7" y="1" width="12" height="5"/><rect x="4" y="6" width="18" height="24" rx="2"/><rect x="8" y="14" width="8" height="9"/></svg></div>
      ALL Indications in<br>ONE product
    </div>
    <div class="feature f2">
      <div class="icon"><svg width="30" height="32" viewBox="0 0 30 32" fill="none" stroke="#0054AA" stroke-width="1.8"><path d="M15 2 27 6v10c0 7-6 12-12 14C9 28 3 23 3 16V6z"/><path d="m9 16 4 4 8-8"/></svg></div>
      Regulatory<br>Freedom
    </div>
    <div class="feature f3">
      <div class="icon"><svg width="32" height="32" viewBox="0 0 32 32" fill="none" stroke="#0054AA" stroke-width="1.8"><path d="M8 4l6 10M5 28h18M9 24h10M13 14c-4 2-5 6-4 10"/><rect x="6" y="2" width="6" height="6" transform="rotate(-30 9 5)"/><circle cx="24" cy="14" r="4"/><circle cx="24" cy="14" r="1.5"/></svg></div>
      cGMP &amp; FDA<br>Registered<br>Laboratory
    </div>
    <div class="feature f4">
      <div class="icon"><svg width="30" height="32" viewBox="0 0 30 32" fill="none" stroke="#0054AA" stroke-width="1.6"><path d="M7 3v8M3 7h8M4 4l6 6M10 4l-6 6"/><rect x="14" y="8" width="10" height="4"/><rect x="12" y="12" width="14" height="18" rx="2"/><rect x="15" y="18" width="7" height="7"/></svg></div>
      Shelf Stable:<br>NO Dry Ice,<br>NO Feezers
    </div>
    <div class="v-rule" style="top:18px;height:104px"></div>
    <div class="v-rule" style="top:146px;height:124px"></div>
    <div class="h-rule" style="left:67px"></div>
    <div class="h-rule" style="left:250px"></div>
  </section>

  <h2 class="abs sub-head">Complete Regenerative Therapy</h2>
  <p class="abs body-copy">A Sophisticated cGMP &amp; FDA Registered laboratory subjects the stem cells to normal biological stressors, causing them to naturally express ALL 30,000+ gene expressions (protein, m/mi/lnc RNA) in the human genome: ALL cytokines, ALL growth factors, etc. These Regenerative Messages are kept in their NATURAL RATIOS of those at birth, nothing synthesized Importantly, these regenerative messages are then isolated, verified, and measured, ensuring that what is collected has no residual DNA or idiosyncratic biomarkers.</p>
  <div class="abs tag-bar"><span>NO KNOWN SIDE EFFECTS</span><span>NO KNOWN CONTRAINDICATIONS</span></div>

  <h2 class="abs reg-head">Cell Factors are NOT<br>regulated class controlled</h2>
  <p class="abs reg-copy">Cell factors per the FDA’s own statements are not a biologic and as such can be categorized alongside other sterile injectable FDA compliant manufactured products like compounded vitamins &amp; minerals. Manufacturing process FD Regulated.</p>

  <div class="abs dash dash-1"></div>

  <div class="abs label label-form"><div class="top">PHYSICAL FORM</div><div class="bottom">Lyophilized POWDER</div></div>
  <div class="abs label label-apps"><div class="top">APPLICATIONS</div><div class="bottom">(ALL LEGAL)</div></div>

  <svg class="abs vial" width="84" height="160" viewBox="0 0 84 160" aria-hidden="true">
    <defs>
      <linearGradient id="glass" x1="0" x2="1"><stop offset="0" stop-color="#e4e8ec"/><stop offset=".5" stop-color="#fbfcfd"/><stop offset="1" stop-color="#d8dde2"/></linearGradient>
      <linearGradient id="cap" x1="0" x2="1"><stop offset="0" stop-color="#7d8084"/><stop offset=".5" stop-color="#c4c6c9"/><stop offset="1" stop-color="#6e7175"/></linearGradient>
    </defs>
    <rect x="18" y="2" width="48" height="22" rx="3" fill="url(#cap)"/>
    <rect x="22" y="24" width="40" height="10" fill="#d5d7da"/>
    <path d="M22 34h40l10 14v104a6 6 0 0 1-6 6H18a6 6 0 0 1-6-6V48z" fill="url(#glass)"/>
    <rect x="12" y="70" width="60" height="60" fill="#f2f4f6" opacity=".9"/>
  </svg>

  <ul class="abs checks checks-form">
    <li>NO DRY ICE (no live cells or DNA)</li>
    <li>NO FREEZERS</li>
    <li>SHELF STABLE -3yr expiration date</li>
  </ul>
  <ul class="abs checks checks-apps">
    <li>IV, IN, IM, NB, IT, IA, SQ, IP, MC.IV</li>
    <li>Intrathecal</li>
    <li>Eye Drops, Hair, Facial</li>
  </ul>

  <div class="abs dash dash-2"></div>

  <h2 class="abs contact-head">Contact us for <span>more information</span></h2>
  <div class="abs contact-line phone">
    <span class="ico"><svg width="11" height="11" viewBox="0 0 24 24" fill="#fff"><path d="M6.6 10.8a15 15 0 0 0 6.6 6.6l2.2-2.2c.3-.3.7-.4 1-.2 1.1.4 2.3.6 3.6.6.6 0 1 .4 1 1V20c0 .6-.4 1-1 1A17 17 0 0 1 3 4c0-.6.4-1 1-1h3.5c.6 0 1 .4 1 1 0 1.3.2 2.5.6 3.6.1.3 0 .7-.2 1z"/></svg></span>
    (555) 014-2290
  </div>
  <div class="abs contact-line email">
    <span class="ico sm"><svg width="8" height="6" viewBox="0 0 8 6" fill="none" stroke="#fff" stroke-width=".9"><rect x=".5" y=".5" width="7" height="5"/><path d="m.5.5 3.5 3 3.5-3"/></svg></span>
    info@VelmoraFARM.com
  </div>
  <div class="abs contact-line web">
    <span class="ico sm"><svg width="9" height="9" viewBox="0 0 10 10" fill="none" stroke="#fff" stroke-width=".8"><circle cx="5" cy="5" r="4"/><path d="M1 5h8M5 1c2 2 2 6 0 8M5 1c-2 2-2 6 0 8"/></svg></span>
    <span>www.<b>VelmoraFARM</b>.com</span>
  </div>
  <div class="abs qr" role="img" aria-label="QR code area linking to the product landing page"></div>

</main>
</body>
</html>
```